依頼詳細
値段は入れず、『不安を安心に』『疑問を納得へ』『生活保護のご葬儀 自己負担0円』と言った文言を入れていただきたいです。
葬儀の流れの図も入れていただきたいです。
※添付ファイルを参照ください。
記載項目
電話番号のところは◯にしておいてください
サイズ
A4
ページ数
片面
希望イメージ
シンプル 複雑
単色 カラフル
暗い 明るい
日常 高級
遊び心 厳粛
未来的 伝統的
女性的 男性的
希望する色
赤系
納品ファイル
• 高解像度JPG (.jpg)
• イラストレーター形式 (.ai)
• フォトショップ形式 (.psd)
• PNG形式 (.png)
補足説明
■ 選んだ理由

シンプルで中身がわかりやすく気に入りました

■ 提案者全員のお礼・コメント

ありがとうございます!!また機会がありましたらお願い致します

```html
<!DOCTYPE html>
<html lang="ja">
<head>
<meta charset="utf-8">
<title>生活保護葬儀</title>
<link rel="stylesheet" href="https://fonts.googleapis.com/css2?family=Noto+Serif+JP:wght@500;700;900&family=Noto+Sans+JP:wght@400;500;700&display=swap">
<style>
:root{
  --purple:#7a5aa8;
  --purple-dark:#5b3f86;
  --lavender:#ebe4f3;
  --lavender-mid:#cdbfe2;
  --ink:#2e2a33;
  --grey:#6b6670;
  --paper:#ffffff;
}
*{margin:0;padding:0;box-sizing:border-box}
html,body{width:851px;height:1200px;overflow:hidden;background:var(--paper)}
body{font-family:"Noto Sans JP",sans-serif;color:var(--ink);position:relative}
.flyer{position:relative;width:851px;height:1200px;overflow:hidden}
.tagline{position:absolute;top:12px;right:26px;font-family:"Noto Serif JP",serif;font-size:14px;color:var(--grey);letter-spacing:.08em}
.flowers{position:absolute;left:0;top:0;width:230px;height:110px;background:radial-gradient(circle at 30% 40%,#d9c9ea,#a98cc9 45%,#f4f0f8 80%)}
.brand{position:absolute;left:20px;top:40px;font-family:"Noto Sans JP",sans-serif;font-weight:700;font-size:14px;color:#fff;letter-spacing:.15em}
.title{position:absolute;top:38px;left:0;width:100%;text-align:center;font-family:"Noto Serif JP",serif;font-weight:900;font-size:64px;letter-spacing:.06em;color:var(--ink)}
.title-rule{position:absolute;top:132px;left:190px;width:470px;height:4px;background:linear-gradient(90deg,transparent,var(--lavender-mid),transparent)}
.intro{position:absolute;top:150px;left:40px;width:490px;font-size:14.5px;line-height:1.75;color:var(--purple-dark);font-weight:500}
.consult{position:absolute;top:145px;right:30px;width:260px;height:100px;background:linear-gradient(180deg,#f3eff8,#e2d8ee);border-radius:6px}
.target{position:absolute;top:258px;left:40px;width:440px;background:var(--lavender);padding:10px 16px;border-radius:4px}
.target-label{display:inline-block;background:var(--purple);color:#fff;font-size:12px;padding:2px 12px;margin-bottom:6px}
.target li{list-style:none;font-size:14px;font-weight:700;color:var(--purple-dark);line-height:1.6}
.target li::before{content:"■ ";color:var(--purple)}
.target small{display:block;font-size:10px;color:var(--grey);line-height:1.5;margin-top:3px}
.zero{position:absolute;top:252px;right:30px;width:290px;height:140px;text-align:center}
.zero-head{background:var(--purple);color:#fff;font-size:15px;font-weight:700;padding:5px 0;border-radius:4px 4px 0 0}
.zero-sub{font-family:"Noto Serif JP",serif;font-size:26px;font-weight:700;color:var(--purple-dark);margin-top:4px}
.zero-amount{font-family:"Noto Serif JP",serif;color:var(--purple);font-weight:900;line-height:1}
.zero-amount b{font-size:86px}
.zero-amount span{font-size:30px}
.section-chip{position:absolute;left:30px;background:var(--purple);color:#fff;font-size:14px;font-weight:700;padding:4px 18px}
.services{position:absolute;top:430px;left:30px;width:791px;display:grid;grid-template-columns:repeat(6,1fr);gap:8px 10px}
.service{text-align:center}
.service-icon{height:40px;border:1px solid var(--lavender-mid);background:#f7f4fb;border-radius:3px}
.service p{font-size:10.5px;color:var(--ink);margin-top:3px;line-height:1.3}
.flow-head{position:absolute;top:578px;left:30px;width:791px;background:var(--purple);color:#fff;font-size:15px;font-weight:700;padding:5px 14px}
.steps{position:absolute;top:612px;left:30px;width:791px}
.step{display:flex;height:64px;align-items:center;border-bottom:1px dashed var(--lavender-mid)}
.step-name{width:200px;height:50px;display:flex;align-items:center;padding-left:14px;background:var(--lavender);font-family:"Noto Serif JP",serif;font-weight:700;font-size:17px;color:var(--purple-dark);clip-path:polygon(0 0,92% 0,100% 50%,92% 100%,0 100%)}
.step-text{flex:1;padding-left:18px;font-size:12px;line-height:1.6}
.step-text.narrow{padding-right:210px}
.phone{font-family:"Noto Sans JP",sans-serif;font-weight:700;font-size:34px;color:var(--purple-dark);margin-left:20px;letter-spacing:.02em}
.note{position:absolute;top:148px;right:0;width:196px;background:var(--lavender);padding:8px 10px;font-size:11px;line-height:1.5;color:var(--purple-dark);border-left:4px solid var(--purple)}
.footer{position:absolute;bottom:0;left:0;width:100%;height:50px;background:var(--purple);color:#fff;font-size:12px;display:flex;align-items:center;justify-content:center;letter-spacing:.05em}
</style>
</head>
<body>
<div class="flyer">
  <div class="flowers" role="img" aria-label="紫の胡蝶蘭の写真"></div>
  <div class="brand">AOBA</div>
  <p class="tagline">不安を安心に、疑問を納得へ。</p>
  <h1 class="title">生活保護葬儀</h1>
  <div class="title-rule"></div>

  <p class="intro">青葉典礼では生活保護受給者の葬儀（火葬式）を承ります。生活保護受給者の方は市区町村福祉事務所・社会保障課に葬祭扶助の申請をすることにより施主様は自己負担なしで御葬儀（火葬式）を執り行うことができます。</p>
  <div class="consult" role="img" aria-label="スタッフがご家族と相談しているイラスト"></div>

  <div class="target">
    <span class="target-label">対象者</span>
    <ul>
      <li>生活保護受給者が亡くなられた場合</li>
      <li>生活保護受給者が葬主になった場合</li>
    </ul>
    <small>※詳しくは福祉事務所へご確認ください。申請手続きもご案内致します。</small>
  </div>

  <div class="zero">
    <div class="zero-head">生活保護のご葬儀</div>
    <div class="zero-sub">自己負担</div>
    <div class="zero-amount"><b>0</b><span>円</span></div>
  </div>

  <div class="section-chip" style="top:400px">サービス</div>
  <div class="services">
    <div class="service"><div class="service-icon" role="img" aria-label="寝台車のアイコン"></div><p>寝台車搬送</p></div>
    <div class="service"><div class="service-icon" role="img" aria-label="書類のアイコン"></div><p>死亡届・火葬許可申請</p></div>
    <div class="service"><div class="service-icon" role="img" aria-label="安置のアイコン"></div><p>ご遺体安置</p></div>
    <div class="service"><div class="service-icon" role="img" aria-label="ドライアイスのアイコン"></div><p>ドライアイス</p></div>
    <div class="service"><div class="service-icon" role="img" aria-label="ワゴン車のアイコン"></div><p>ワゴン車搬送</p></div>
    <div class="service"><div class="service-icon" role="img" aria-label="棺のアイコン"></div><p>棺一式</p></div>
    <div class="service"><div class="service-icon" role="img" aria-label="シーツのアイコン"></div><p>仏衣・シーツ</p></div>
    <div class="service"><div class="service-icon" role="img" aria-label="骨壺のアイコン"></div><p>骨壺・骨箱</p></div>
    <div class="service"><div class="service-icon" role="img" aria-label="火葬場のアイコン"></div><p>火葬料金</p></div>
    <div class="service"><div class="service-icon" role="img" aria-label="花のアイコン"></div><p>枕花</p></div>
    <div class="service"><div class="service-icon" role="img" aria-label="スタッフのアイコン"></div><p>運営スタッフ</p></div>
    <div class="service"><div class="service-icon" role="img" aria-label="位牌のアイコン"></div><p>白木位牌</p></div>
  </div>

  <div class="flow-head">生活保護葬儀の流れ</div>
  <div class="steps">
    <div class="step"><div class="step-name">1.ご臨終</div><div class="step-text">ご連絡は24時間受付</div><span class="phone">0120-000-000</span></div>
    <div class="step"><div class="step-name">2.お迎え</div><div class="step-text">ご指定の場所へ寝台車でお迎えにあがり、安置場所へお連れします。</div></div>
    <div class="step"><div class="step-name">3.ご遺体・ご遺体安置</div><div class="step-text narrow">ご自宅または安置施設にご遺体を安置し、ドライアイスで保全致します。</div></div>
    <div class="step"><div class="step-name">4.お打合せ</div><div class="step-text narrow">担当者が火葬の日時やご希望を伺い、必要な手続きをご説明します。</div></div>
    <div class="step"><div class="step-name">5.出棺・火葬</div><div class="step-text">ご納棺の後、火葬場へ出棺し火葬を執り行います。（所要時間 約1〜2時間）</div></div>
    <div class="step"><div class="step-name">6.ご収骨</div><div class="step-text">火葬後、ご遺族の皆様でご遺骨を骨壺へお納めいただきます。</div></div>
    <div class="step"><div class="step-name">7.ご返骨</div><div class="step-text">ご遺骨はご遺族様へお渡しします。納骨先のご相談も承ります。</div></div>
    <div class="step"><div class="step-name" style="font-size:13px">8.生活保護葬儀のご請求手続き</div><div class="step-text">葬祭扶助の請求手続きは当社が代行致しますのでご安心ください。</div></div>
    <div class="note">★ 死亡届提出、火葬許可証の受け取りなどの手続きは当社が代行致します。</div>
  </div>

  <div class="footer">ご相談・お見積りは無料です。どうぞお気軽にお問い合わせください。　青葉典礼</div>
</div>
</body>
</html>
```